Children's Party Business needs a Business Card design!

We need a double sided, colour business card design.
The company name is "Bright Lantern Kids Events". We want one side to feature this logo.
We want the second side to feature the two branches "The Caped Crusade Adventure" and "The Fairy Glade Adventure". I have attached logos for each of these below. When using these, I suggest removing the tagline & image from the logos, as those elements are already featured in the "Bright Lantern Kids Event" logo.
To be included:
www.brightlanternkidsevents.com.au
1300 481 607
Optional text- "Making Dreams a Reality"
Optional photos- I've attached a bunch of our Character photos, which can be used if you please!
To give you an idea of the business, see The Caped Crusade Adventure website (under development):
http://qorvintel.com/demo/capedcrusadeadventure/
Target Market(s)
Parents
Industry/Entity Type
Business
Contact Information for Business Card
To be included:
1300 481 607
Colors
Designer to choose colors to be used in the design.
Look and feel

```html
<!DOCTYPE html>
<html lang="en">
<head>
<meta charset="utf-8">
<title>Bright Lantern Kids Events — Business Card</title>
<link rel="stylesheet" href="https://fonts.googleapis.com/css2?family=Fredoka:wght@600&family=Open+Sans+Condensed:wght@300&family=Handlee&display=swap">
<style>
  :root {
    --page: #ece8e2;
    --card-white: #ffffff;
    --card-dark: #333335;
    --card-dark-deep: #232325;
    --brand-navy: #3b4a9a;
    --band-pink: #e23d8c;
    --band-purple: #9a7fd1;
    --tagline: #8f76c4;
    --contact: #f2f2f2;
    --icon: #e23d5e;
    --caped: #f7c51e;
    --glade: #f05a9b;
    --art-blue: #4e5ea8;
    --art-sky: #8fd3ee;
  }
  * { box-sizing: border-box; margin: 0; padding: 0; }
  html, body { width: 771px; height: 1200px; overflow: hidden; }
  body {
    background: var(--page);
    position: relative;
  }
  .card {
    position: absolute;
    left: 75px;
    width: 620px;
    height: 379px;
    border-radius: 6px;
    overflow: hidden;
    box-shadow: 0 6px 18px rgba(0,0,0,0.18);
  }
  .card--front { top: 181px; background: var(--card-white); }
  .card--back {
    top: 640px;
    background: linear-gradient(160deg, var(--card-dark) 0%, var(--card-dark-deep) 100%);
  }
  .card__shapes { position: absolute; inset: 0; width: 100%; height: 100%; }

  .art {
    position: absolute;
    border-radius: 40% 40% 30% 30%;
  }
  .art--hero {
    left: 40px; top: 150px; width: 130px; height: 150px;
    background: linear-gradient(180deg, var(--art-sky) 0%, var(--art-blue) 60%);
    opacity: 0.85;
  }
  .art--fairy {
    left: 340px; top: 28px; width: 110px; height: 90px;
    background: linear-gradient(135deg, var(--art-sky) 0%, var(--art-blue) 100%);
    opacity: 0.8;
  }

  .brand-name {
    position: absolute;
    left: 170px; top: 118px;
    width: 260px;
    font-family: "Fredoka", sans-serif;
    font-weight: 600;
    font-size: 38px;
    line-height: 1.02;
    color: var(--brand-navy);
    text-align: center;
  }

  .contact {
    position: absolute;
    right: 36px; top: 282px;
    list-style: none;
    font-family: "Open Sans Condensed", sans-serif;
    font-weight: 300;
    color: var(--contact);
  }
  .contact__item {
    display: flex; align-items: center; justify-content: flex-end;
    gap: 10px;
    margin-bottom: 14px;
  }
  .contact__item--phone { font-size: 26px; letter-spacing: 1px; }
  .contact__item--web { font-size: 19px; }
  .contact__icon { width: 18px; height: 18px; flex: none; }

  .tagline-text {
    font-family: "Handlee", cursive;
    font-size: 20px;
    fill: var(--tagline);
  }

  .experience {
    position: absolute;
    font-family: "Fredoka", sans-serif;
    font-weight: 600;
    line-height: 1;
  }
  .experience--caped {
    left: 60px; top: 78px;
    font-size: 46px;
    color: var(--caped);
  }
  .experience--glade {
    left: 170px; top: 210px;
    font-size: 40px;
    color: var(--glade);
  }
</style>
</head>
<body>

  <section class="card card--front" aria-label="Business card front">
    <svg class="card__shapes" viewBox="0 0 620 379" aria-hidden="false">
      <defs>
        <linearGradient id="band-gradient" x1="0" y1="1" x2="1" y2="0">
          <stop offset="0" stop-color="var(--band-pink)"/>
          <stop offset="1" stop-color="var(--band-purple)"/>
        </linearGradient>
        <linearGradient id="dark-gradient" x1="0" y1="0" x2="1" y2="1">
          <stop offset="0" stop-color="#3a3a3c"/>
          <stop offset="1" stop-color="#262628"/>
        </linearGradient>
        <path id="tagline-curve" d="M330 262 C450 210 545 145 600 70"/>
      </defs>
      <path class="dark-panel" d="M130 379 C330 300 520 200 620 30 L620 379 Z" fill="url(#dark-gradient)"/>
      <path class="colour-band" d="M130 379 C330 300 520 200 620 30" fill="none" stroke="url(#band-gradient)" stroke-width="7"/>
      <text class="tagline-text"><textPath href="#tagline-curve" startOffset="12%">Making Dreams a Reality</textPath></text>
    </svg>

    <div class="art art--hero" role="img" aria-label="Illustration of a caped superhero holding colourful balloons"></div>
    <div class="art art--fairy" role="img" aria-label="Illustration of a flying fairy with wings"></div>

    <h1 class="brand-name">Bright Lantern Kids Events</h1>

    <ul class="contact">
      <li class="contact__item contact__item--phone">
        <svg class="contact__icon" viewBox="0 0 20 20" aria-hidden="true">
          <path d="M5 2h3l1.5 4-2 1.5a10 10 0 0 0 5 5L14 10.5l4 1.5v3a2 2 0 0 1-2 2A14 14 0 0 1 3 4a2 2 0 0 1 2-2z" fill="var(--icon)"/>
        </svg>
        <span>1300 481 607</span>
      </li>
      <li class="contact__item contact__item--web">
        <svg class="contact__icon" viewBox="0 0 20 20" aria-hidden="true">
          <g fill="none" stroke="var(--icon)" stroke-width="1.6">
            <circle cx="10" cy="10" r="8"/>
            <ellipse cx="10" cy="10" rx="3.5" ry="8"/>
            <path d="M2 10h16M3.5 6h13M3.5 14h13"/>
          </g>
        </svg>
        <span>www.brightlanternkidsevents.com.au</span>
      </li>
    </ul>
  </section>

  <section class="card card--back" aria-label="Business card back">
    <h2 class="experience experience--caped">The Caped Crusade<br>Adventure</h2>
    <h2 class="experience experience--glade">The Fairy Glade<br>Adventure</h2>
  </section>

</body>
</html>
```